I need a Cool Physio Postcard / Flyer

HI!
We need a double sided, postcard sized, promotional card (not an actual postcard) to distribute to gyms and sporting clubs, promoting our physiotherapy clinic.
The main colours of our brand are navy blue & white (As seen in sample files).
I want it to be HORIZONTAL
On one side i'd like our logo / image.
The name - "Heel & Stride Recovery Australia" and the tagline - "“Australia’s trusted lower limb recovery team.”
• Fast Rehab for lower limb injury and surgery
• Mobilisation of the foot and ankle
• Hands on therapy
• National sporting team expertise
• Podiatry (Toe-nail, skin, diabetic foot care, orthotics)
• Video pressure treadmill gait analysis and correction
• Running assessment
• Nordic walking training and sessions
Also our website: www.HSRA-demo.com.au & a Pagebook icon next to www.Pagebook-demo.com/HSRA
Also see the sample image of the runner and blue colouring. I would like this included somewhere on the postcard. I'd like to see some different design options implementing the image in different ways (front or back).
On the other side of the card I want the following text:
"HSRA is Victoria’s leading specialist provider of rehabilitation for Foot & Ankle injury and surgery.
We see our patients through their rehabilitation with an unmatched level of care and expertise.
Whether you’re an elite athlete, a weekend walker or strolling to the office, we provide the highest quality treatment and support to quickly get you back to your usual functional capacity, moving pain free with confidence.
Make an appointment at one of our FOUR Victorian locations today!”
Richmond
Summit Motion Clinic
Level 1, 418 Wattle St
Richmond 3121
1300 642 913 Frankston
Suite 6, 371 Pemberton Drive
Frankston 3199
9483 2295
Brighton
Suite 4, 937 Elm Street
Brighton 3186
9371 4058
Geelong
146 Kingsley Terrace
Geelong 3220
5264 3719
Please display our four locations in a similar fashion to the white screenshot ive attached.
The images I included of my draft design are just to provide you an idea or some inspiration of what I’m after. Please feel free to use your creativity.. Good Luck!
Reason: I accidentally didn't put a design brief in for the first 6 days of the project. The designs only started arriving 4 days ago once I corrected this mistake.
I need more time to provide feedback & get exactly what I want.
Thanks in advance
Reid

```html
<!DOCTYPE html>
<html lang="en">
<head>
<meta charset="utf-8">
<title>Heel &amp; Stride Recovery Australia – Promo Card</title>
<link href="https://fonts.googleapis.com/css2?family=Open+Sans:wght@400;600&display=swap" rel="stylesheet">
<style>
:root{
  --page:#e9ebee;
  --navy:#163e66;
  --navy-deep:#0f2f52;
  --blue:#2a5f92;
  --blue-mid:#336ea3;
  --blue-light:#8fb3d6;
  --sky:#c9dbee;
  --white:#ffffff;
  --text-soft:#dbe7f4;
}
*{box-sizing:border-box;margin:0;padding:0}
html,body{width:1200px;height:1000px;overflow:hidden}
body{background:var(--page);font-family:"Open Sans",Arial,sans-serif;color:var(--white)}
.card{position:absolute;left:100px;top:180px;width:1000px;height:640px;display:flex;box-shadow:0 10px 30px rgba(0,0,0,.25);overflow:hidden}
.panel{position:relative;width:500px;height:640px;overflow:hidden}
.panel--front{background:var(--navy)}
.panel--back{background:var(--navy-deep)}
.hero{position:absolute;left:0;top:0;width:500px;height:360px;background:radial-gradient(ellipse at 55% 45%,#e6eef7 0%,#8fb0d2 30%,#3a6a9a 62%,#163e66 100%)}
.brand{position:absolute;left:0;top:26px;width:500px;text-align:center}
.brand__name{font-size:25px;font-weight:600;line-height:32px;padding-bottom:6px;border-bottom:1px solid var(--white);display:inline-block}
.brand__tagline{font-size:11px;font-weight:400;letter-spacing:1px;margin-top:6px;text-transform:uppercase}
.logo-tile{position:absolute;right:30px;top:270px;width:130px;height:80px;background:var(--white);display:flex;align-items:center;justify-content:center;text-align:center;padding:8px}
.logo-tile span{font-size:10px;font-weight:600;line-height:14px;color:var(--navy)}
.services{position:absolute;left:40px;top:385px;list-style:none;font-size:14px;line-height:22px}
.services li::before{content:"•";margin-right:12px;color:var(--sky)}
.social{position:absolute;left:0;bottom:0;width:500px;height:40px;background:var(--blue-light);display:flex;align-items:center;padding-left:20px;gap:10px;font-size:12px;color:var(--navy)}
.social__mark{width:14px;height:14px;background:var(--navy);flex:none}
.band{position:absolute;transform:skewY(-12deg)}
.band--a{left:-40px;top:40px;width:600px;height:50px;background:var(--blue-mid)}
.band--b{left:-40px;top:390px;width:600px;height:60px;background:var(--blue)}
.band--c{left:-40px;top:590px;width:600px;height:120px;background:var(--blue-light)}
.intro{position:absolute;left:40px;top:108px;width:420px;font-size:13px;line-height:19px;color:var(--text-soft)}
.intro p{margin-bottom:10px}
.cta{position:absolute;left:40px;top:302px;width:420px;font-size:19px;line-height:25px;font-weight:600;text-align:center}
.locations{position:absolute;left:40px;top:384px;width:420px;display:flex;justify-content:space-between;font-size:13px;line-height:18px}
.locations__col--right{text-align:right}
.location{margin-bottom:14px}
</style>
</head>
<body>
<main class="card">
  <section class="panel panel--front">
    <div class="hero" role="img" aria-label="Silhouette of a runner against a bright blue sky"></div>
    <header class="brand">
      <div class="brand__name">Heel &amp; Stride Recovery Australia</div>
      <div class="brand__tagline">“Australia’s trusted lower limb recovery team.”</div>
    </header>
    <div class="logo-tile" role="img" aria-label="Clinic logo area"><span>Heel &amp; Stride Recovery Australia</span></div>
    <ul class="services">
      <li>Fast Rehab for lower limb injury and surgery</li>
      <li>Mobilisation of the foot and ankle</li>
      <li>Hands on therapy</li>
      <li>National sporting team expertise</li>
      <li>Podiatry (Toe-nail, skin, diabetic foot care, orthotics)</li>
      <li>Video pressure treadmill gait analysis and correction</li>
      <li>Running assessment</li>
      <li>Nordic walking training and sessions</li>
    </ul>
    <footer class="social"><span class="social__mark"></span>www.Pagebook-demo.com/HSRA or Visit www.HSRA-demo.com.au</footer>
  </section>
  <section class="panel panel--back">
    <div class="band band--a"></div>
    <div class="band band--b"></div>
    <div class="band band--c"></div>
    <div class="intro">
      <p>HSRA is Victoria’s leading specialist provider of rehabilitation for Foot &amp; Ankle injury and surgery.</p>
      <p>We see our patients through their rehabilitation with an unmatched level of care and expertise.</p>
      <p>Whether you’re an elite athlete, a weekend walker or strolling to the office, we provide the highest quality treatment and support to quickly get you back to your usual functional capacity, moving pain free with confidence.</p>
    </div>
    <p class="cta">Make an appointment at one of our FOUR Victorian locations today!</p>
    <div class="locations">
      <div class="locations__col">
        <div class="location">Richmond<br>Level 1, 418 Wattle St<br>Richmond 3121<br>1300 642 913</div>
        <div class="location">Brighton<br>Suite 4, 937 Elm Street<br>Brighton 3186<br>9371 4058</div>
      </div>
      <div class="locations__col locations__col--right">
        <div class="location">Frankston<br>Suite 6, 371 Pemberton Drive<br>Frankston 3199<br>9483 2295</div>
        <div class="location">Geelong<br>146 Kingsley Terrace<br>Geelong 3220<br>5264 3719</div>
      </div>
    </div>
  </section>
</main>
</body>
</html>
```